wealth management firm, professional group, new model

we have a logo that works but we need a card, white background using our colors...clean look

our tag line if can be used in

The Bridge From Client to Owner

```html
<!DOCTYPE html>
<html lang="en">
<head>
<meta charset="utf-8">
<title>Arcova Wealth Partners – Business Card</title>
<link href="https://fonts.googleapis.com/css2?family=Montserrat:wght@400&family=Lato:wght@300&display=swap" rel="stylesheet">
<style>
  :root {
    --navy: #1a2b4c;
    --band: #172d4f;
    --paper: #ffffff;
    --backdrop: #f1f2f4;
  }
  html, body {
    margin: 0;
    padding: 0;
    width: 1200px;
    height: 1200px;
    overflow: hidden;
    background: var(--backdrop);
  }
  .canvas {
    position: relative;
    width: 1200px;
    height: 1200px;
  }
  .card {
    position: absolute;
    left: 171px;
    width: 858px;
    height: 504px;
    background: var(--paper);
    overflow: hidden;
  }
  .card--front { top: 72px; }
  .card--back  { top: 622px; }

  .brand {
    position: absolute;
    left: 0;
    width: 440px;
    top: 232px;
    text-align: center;
    color: var(--navy);
    font-family: "Montserrat", sans-serif;
    font-weight: 400;
  }
  .brand__name {
    font-size: 40px;
    letter-spacing: 0.32em;
    line-height: 1;
    margin: 0 0 0 0.32em;
  }
  .brand__descriptor {
    font-size: 16px;
    letter-spacing: 0.14em;
    margin-top: 26px;
  }

  .divider-arc {
    position: absolute;
    left: 0;
    top: 0;
    width: 858px;
    height: 504px;
  }

  .contact {
    position: absolute;
    left: 520px;
    top: 0;
    color: var(--navy);
    font-family: "Lato", sans-serif;
    font-weight: 300;
    font-size: 21px;
    line-height: 1.3;
  }
  .contact__row {
    position: absolute;
    left: 0;
    display: flex;
    align-items: flex-start;
    white-space: nowrap;
  }
  .contact__icon {
    width: 14px;
    height: 14px;
    margin-top: 7px;
    margin-right: 8px;
    flex: none;
    fill: var(--navy);
  }
  .contact__row--web     { top: 158px; }
  .contact__row--phone   { top: 198px; }
  .contact__row--email   { top: 238px; }
  .contact__row--address { top: 292px; }

  .band {
    position: absolute;
    left: 0;
    top: 110px;
    width: 858px;
    height: 285px;
    background: var(--band);
    display: flex;
    align-items: center;
    justify-content: center;
  }
  .band__name {
    color: var(--paper);
    font-family: "Montserrat", sans-serif;
    font-weight: 400;
    font-size: 56px;
    letter-spacing: 0.32em;
    margin-left: 0.32em;
  }
</style>
</head>
<body>
<main class="canvas">

  <section class="card card--front" aria-label="Card front">
    <div class="brand">
      <div class="brand__name">ARCOVA</div>
      <div class="brand__descriptor">WEALTH PARTNERS</div>
    </div>

    <svg class="divider-arc" viewBox="0 0 858 504" aria-hidden="true">
      <path d="M519 52 Q353 252 519 452" fill="none" stroke="#1a2b4c" stroke-width="2.5"/>
    </svg>

    <address class="contact" style="font-style:normal">
      <div class="contact__row contact__row--web">
        <svg class="contact__icon" viewBox="0 0 16 16" aria-hidden="true">
          <circle cx="8" cy="8" r="7"/>
          <path d="M1 8h14M8 1c-3 3.5-3 10.5 0 14M8 1c3 3.5 3 10.5 0 14" stroke="#fff" stroke-width="1.1" fill="none"/>
        </svg>
        <span>Arcova.net</span>
      </div>
      <div class="contact__row contact__row--phone">
        <svg class="contact__icon" viewBox="0 0 16 16" aria-hidden="true">
          <path d="M3.2 1.2l2.4 0 1.2 3.4-1.6 1.2c.8 1.8 2.2 3.2 4 4l1.2-1.6 3.4 1.2 0 2.4c0 .9-.8 1.6-1.7 1.5C6.2 12.8 3.2 9.8 1.7 2.9 1.6 2 2.3 1.2 3.2 1.2z"/>
        </svg>
        <span>620-555-014</span>
      </div>
      <div class="contact__row contact__row--email">
        <svg class="contact__icon" viewBox="0 0 16 16" aria-hidden="true">
          <path d="M1 3h14v10H1z"/>
          <path d="M1.5 3.5L8 8.5l6.5-5" stroke="#fff" stroke-width="1.3" fill="none"/>
        </svg>
        <span>info@arcova.net</span>
      </div>
      <div class="contact__row contact__row--address">
        <svg class="contact__icon" viewBox="0 0 16 16" aria-hidden="true">
          <path d="M8 1a5 5 0 0 0-5 5c0 4 5 9 5 9s5-5 5-9a5 5 0 0 0-5-5z"/>
          <circle cx="8" cy="6" r="1.8" fill="#fff"/>
        </svg>
        <span>48 W 9th Ave, Ste 210<br>Salina, KS 67401</span>
      </div>
    </address>
  </section>

  <section class="card card--back" aria-label="Card back">
    <div class="band">
      <span class="band__name">ARCOVA</span>
    </div>
  </section>

</main>
</body>
</html>
```